Quotation and Scripture Design

We are a marketing firm looking for a graphic designer who is gifted in the merging of typestyles, colors, and composition into images suitable for framing in the home or office. The design criteria is quite simple, (1) keep it fresh without looking dated or religious, and (2) push the envelope a little with good, solid graphic design. Phase one will involve building our inventory of original artwork to fifty or more pieces to be marketed online. For phase two in addition to a line of greeting cards, we will also offer art pieces reproduced by laser engravers, CNC routers, chemical etching, and digital printers. For this reason it is necessary that all art files be submitted in a vector format.

Target Market(s)

Professional women and men who appreciate and purchase gallery quality artwork.

Industry/Entity Type

Graphic Designer

Requirements
Must have
• Selection of the designer will be based on their graphic interruption of the following two quotations.
Quotation No. 1 - Romans 8:28
And we know that all things work together for good to those who love God, to those who are called according to His purpose.
Quotation No. 2 -Jeremiah 29:11
For I know the plans I have for you, declares the Lord. Plans to prosper you and not to harm you. Plans to give you hope and a future.
Design one of these two formats to fit a 8" x10" frame, and the other to fit a 12" x 12" frame.
Nice to have
• Rich colors, fresh typestyles . . . please no Times Roman. Bold, creative composition is what we are looking for.
Should not have
• Dated, religious artwork found in the local bible bookstore is a very good example of what we DO NOT want. If it is not something you would purchase for yourself or a friend, more than likely it won't meet our criteria.

```html
<!DOCTYPE html>
<html lang="en">
<head>
<meta charset="utf-8">
<title>Jeremiah 29:11 – Plans and a Future</title>
<link rel="stylesheet" href="https://fonts.googleapis.com/css2?family=Graduate&display=swap">
<style>
  :root {
    --sky-top: #d6dccf;
    --sky-mid: #c3ccc4;
    --cloud-blue: #a9b8bf;
    --horizon: #cfd0c4;
    --grass: #a08d76;
    --grass-deep: #7d6a58;
    --ink-white: #ffffff;
    --frame-white: rgba(255, 255, 255, 0.55);
    --label-ink: #5b4a40;
  }
  * { margin: 0; padding: 0; box-sizing: border-box; }
  html, body {
    width: 958px;
    height: 1200px;
    overflow: hidden;
    background: var(--sky-top);
  }
  .poster {
    position: relative;
    width: 958px;
    height: 1200px;
    overflow: hidden;
    font-family: 'Graduate', 'Rockwell', serif;
    color: var(--ink-white);
  }
  .poster__photo {
    position: absolute;
    inset: 0;
    background:
      radial-gradient(ellipse 60% 30% at 75% 45%, rgba(169,184,191,0.55), transparent 70%),
      radial-gradient(ellipse 70% 25% at 20% 55%, rgba(225,228,218,0.6), transparent 70%),
      linear-gradient(180deg,
        var(--sky-top) 0%,
        var(--sky-mid) 35%,
        var(--cloud-blue) 55%,
        var(--horizon) 72%,
        var(--grass) 84%,
        var(--grass-deep) 100%);
  }
  .poster__frame {
    position: absolute;
    inset: 0;
    pointer-events: none;
  }
  .verse-line {
    position: absolute;
    left: 0;
    width: 100%;
    text-align: center;
    line-height: 1;
    white-space: nowrap;
    text-transform: uppercase;
    letter-spacing: 0.03em;
  }
  .verse-line--solid { color: var(--ink-white); -webkit-text-stroke: 1px var(--ink-white); }
  .verse-line--soft { color: rgba(255, 255, 255, 0.88); -webkit-text-stroke: 1px rgba(255, 255, 255, 0.88); }
  .verse-line--outline {
    color: transparent;
    -webkit-text-stroke: 2px var(--ink-white);
  }
  .verse-line--opening { font-size: 50px; }
  .verse-line--promise { font-size: 50px; }
  .reference {
    position: absolute;
    left: 345px;
    top: 1095px;
    width: 269px;
    height: 42px;
    background: var(--ink-white);
    color: var(--label-ink);
    font-size: 22px;
    line-height: 42px;
    text-align: center;
    text-transform: uppercase;
    letter-spacing: 0.02em;
    -webkit-text-stroke: 0.6px var(--label-ink);
  }
</style>
</head>
<body>
  <main class="poster">
    <div class="poster__photo" role="img" aria-label="Photograph of a woman in a white shirt jumping joyfully with arms raised against a cloudy sky above a field of wild grass and flowers"></div>

    <svg class="poster__frame" width="958" height="1200" viewBox="0 0 958 1200">
      <rect x="25" y="25" width="908" height="1150" fill="none" stroke="var(--frame-white)" stroke-width="22"/>
    </svg>

    <p class="verse-line verse-line--solid verse-line--opening" style="top:59px;">For I know the plans</p>
    <p class="verse-line verse-line--solid verse-line--opening" style="top:115px;">I have for you,</p>
    <p class="verse-line verse-line--outline verse-line--opening" style="top:170px;">declares the Lord</p>

    <p class="verse-line verse-line--soft verse-line--promise" style="top:770px;">Plans to prosper you</p>
    <p class="verse-line verse-line--soft verse-line--promise" style="top:827px;">and not to harm you</p>
    <p class="verse-line verse-line--outline verse-line--promise" style="top:898px;">Plans to give you</p>
    <p class="verse-line verse-line--outline verse-line--promise" style="top:951px;">hope and a future</p>

    <p class="reference">Jeremiah 29:11</p>
  </main>
</body>
</html>
```